Need an event poster for an automotive event.
The event is a half mile trap speed event. Sometimes called a MaxPace event, they have a 1/2 mile to see how fast They can go. They run one car at a time, it is not a side-by-side race.
Title of the event is “RVLO Sidevalve Autumn Classic”. Dates are October 3-4 2020. Location Blytheville Arkansas. Website is RVLOstretch.com. Most participants will be 50 and older .
All entries must be a carbureted flathead engine .

```html
<!DOCTYPE html>
<html lang="en">
<head>
<meta charset="utf-8">
<title>RVLO Sidevalve Autumn Classic</title>
<link rel="stylesheet" href="https://fonts.googleapis.com/css2?family=Bebas+Neue&family=Montserrat:wght@800&family=Roboto:wght@400;700&display=swap">
<style>
  :root {
    --ink: #1c1d1b;
    --ink-deep: #141513;
    --lime: #8cc63f;
    --lime-bright: #9bd12a;
    --olive: #4c6a16;
    --olive-deep: #2e3f10;
    --white: #ffffff;
    --haze: #d9d9d9;
  }
  * { margin: 0; padding: 0; box-sizing: border-box; }
  html, body { width: 900px; height: 1200px; overflow: hidden; background: var(--ink); }
  .poster {
    position: relative;
    width: 900px;
    height: 1200px;
    overflow: hidden;
    background: radial-gradient(ellipse at 40% 45%, #262725 0%, var(--ink) 55%, var(--ink-deep) 100%);
    color: var(--white);
    font-family: "Roboto", Arial, sans-serif;
  }
  .backdrop { position: absolute; inset: 0; width: 900px; height: 1200px; }
  .texture { position: absolute; }
  .texture-top { left: 120px; top: -80px; width: 320px; height: 240px; }
  .texture-side { left: -100px; top: 560px; width: 220px; height: 320px; }
  .event-title {
    position: absolute;
    left: 165px;
    top: 222px;
    font-family: "Bebas Neue", "Arial Narrow", sans-serif;
    font-weight: 400;
    font-size: 90px;
    line-height: 0.92;
    letter-spacing: 3px;
    text-transform: uppercase;
  }
  .venue {
    position: absolute;
    left: 165px;
    top: 428px;
    display: flex;
    gap: 14px;
    font-weight: 700;
    font-size: 34px;
    line-height: 50px;
  }
  .venue-pin { width: 34px; height: 46px; margin-top: 4px; flex: none; }
  .event-dates {
    position: absolute;
    left: 165px;
    top: 592px;
    font-family: "Montserrat", Arial, sans-serif;
    font-weight: 800;
    font-size: 84px;
    line-height: 1;
    letter-spacing: 2px;
    color: var(--lime);
  }
  .entry-notes { position: absolute; left: 166px; top: 818px; }
  .entry-notes .lead { font-size: 20px; line-height: 28px; }
  .entry-notes .age {
    font-weight: 700;
    font-size: 38px;
    line-height: 48px;
    color: var(--lime);
    margin: 12px 0 8px;
  }
  .entry-notes .rule { font-size: 29px; line-height: 39px; }
  .organiser {
    position: absolute;
    left: 630px;
    top: 1010px;
    display: flex;
    flex-direction: column;
    align-items: flex-start;
    gap: 10px;
  }
  .organiser-name {
    display: flex;
    align-items: center;
    gap: 14px;
    font-weight: 700;
    font-size: 66px;
    line-height: 1;
    letter-spacing: 2px;
  }
  .organiser-dot { width: 28px; height: 28px; border-radius: 50%; background: var(--white); }
  .organiser-web { font-weight: 700; font-size: 22px; letter-spacing: 1px; padding-left: 42px; }
</style>
</head>
<body>
  <main class="poster">
    <svg class="backdrop" viewBox="0 0 960 1280" aria-hidden="true">
      <defs>
        <linearGradient id="corner-green" x1="0" y1="0" x2="1" y2="1">
          <stop offset="0" stop-color="#9bd12a"/>
          <stop offset="1" stop-color="#3f5a12"/>
        </linearGradient>
        <linearGradient id="slope-green" x1="1" y1="0" x2="0" y2="1">
          <stop offset="0" stop-color="#2e3f10"/>
          <stop offset="0.5" stop-color="#6f9a22"/>
          <stop offset="1" stop-color="#9bd12a"/>
        </linearGradient>
        <linearGradient id="slope-light" x1="1" y1="0" x2="0" y2="1">
          <stop offset="0" stop-color="#8cc63f"/>
          <stop offset="1" stop-color="#4c6a16"/>
        </linearGradient>
      </defs>
      <polygon points="0,0 250,0 0,460" fill="url(#corner-green)"/>
      <polygon points="250,0 300,0 0,550 0,460" fill="#2a3a0e" opacity="0.6"/>
      <circle cx="548" cy="-10" r="78" fill="none" stroke="var(--olive)" stroke-width="10"/>
      <circle cx="20" cy="680" r="110" fill="none" stroke="var(--lime)" stroke-width="10"/>
      <polygon points="960,330 960,1280 520,1280" fill="url(#slope-green)"/>
      <polygon points="960,640 960,1280 700,1280" fill="url(#slope-light)" opacity="0.85"/>
      <line x1="745" y1="670" x2="960" y2="345" stroke="var(--lime-bright)" stroke-width="14"/>
      <line x1="785" y1="530" x2="860" y2="415" stroke="var(--olive)" stroke-width="10"/>
      <line x1="440" y1="1175" x2="545" y2="1000" stroke="var(--olive)" stroke-width="10"/>
    </svg>

    <svg class="texture texture-top" viewBox="0 0 320 240" role="img" aria-label="Diagonal stripe texture filling a half disc">
      <defs>
        <radialGradient id="haze-top" cx="0.5" cy="0.4" r="0.6">
          <stop offset="0" stop-color="#d9d9d9" stop-opacity="0.35"/>
          <stop offset="1" stop-color="#d9d9d9" stop-opacity="0.08"/>
        </radialGradient>
      </defs>
      <circle cx="160" cy="80" r="150" fill="url(#haze-top)"/>
    </svg>

    <svg class="texture texture-side" viewBox="0 0 220 320" role="img" aria-label="Diagonal stripe texture filling a disc">
      <defs>
        <radialGradient id="haze-side" cx="0.5" cy="0.5" r="0.6">
          <stop offset="0" stop-color="#d9d9d9" stop-opacity="0.3"/>
          <stop offset="1" stop-color="#d9d9d9" stop-opacity="0.06"/>
        </radialGradient>
      </defs>
      <circle cx="110" cy="170" r="105" fill="url(#haze-side)"/>
    </svg>

    <h1 class="event-title">Sidevalve Autumn<br>Classic</h1>

    <p class="venue">
      <svg class="venue-pin" viewBox="0 0 34 46" aria-hidden="true">
        <path d="M17 2C9 2 3 8 3 16c0 10 14 27 14 27s14-17 14-27C31 8 25 2 17 2z" fill="none" stroke="var(--lime)" stroke-width="2.5"/>
        <circle cx="17" cy="16" r="5" fill="none" stroke="var(--lime)" stroke-width="2.5"/>
      </svg>
      <span>Blytheville Arkansas<br>1/2 mile speed Trials</span>
    </p>

    <p class="event-dates">OCTOBER<br>3-4 2020</p>

    <div class="entry-notes">
      <p class="lead">Most participants will be</p>
      <p class="age">50 and older.</p>
      <p class="rule">All entries must<br>be a carbureted<br>flathead engine</p>
    </div>

    <div class="organiser">
      <p class="organiser-name"><span class="organiser-dot"></span><span>RVLO</span></p>
      <p class="organiser-web">RVLOstretch.com</p>
    </div>
  </main>
</body>
</html>
```